Stationary Design using supplied logo

24 Hour Completion required after acceptance

Business Cards
Letter Head
With Compliments Slips
Web Page Theme

Please only use a the following colors:

Red
Charcoal
Chrome/Silver
White

Red being the DOMINANT Color

Please email questions you may have.

Continued work available to suitably motivated designer.

Industry/Entity Type

Business

```html
<!DOCTYPE html>
<html lang="en">
<head>
<meta charset="utf-8">
<title>Letterhead</title>
<link rel="stylesheet" href="https://fonts.googleapis.com/css2?family=Roboto+Slab:wght@400;700&display=swap">
<style>
  :root {
    --red: #d9261c;
    --charcoal: #2e3a44;
    --paper: #ffffff;
    --paper-tint: #f6f6f6;
    --white: #ffffff;
  }
  html, body {
    margin: 0;
    padding: 0;
    overflow: hidden;
    background: var(--paper);
  }
  .letterhead {
    position: relative;
    width: 849px;
    height: 1200px;
    overflow: hidden;
    background: var(--paper);
    font-family: "Roboto Slab", Georgia, serif;
  }
  .letterhead__texture {
    position: absolute;
    inset: 0;
    background: linear-gradient(180deg, var(--paper-tint), var(--paper) 45%, var(--paper-tint));
  }
  .letterhead__bands {
    position: absolute;
    inset: 0;
  }
  .brand {
    position: absolute;
    left: 54px;
    top: 86px;
    display: flex;
    align-items: center;
    gap: 12px;
  }
  .brand__dot {
    width: 22px;
    height: 22px;
    border-radius: 50%;
    background: var(--red);
  }
  .brand__name {
    font-size: 46px;
    font-weight: 400;
    color: var(--charcoal);
    line-height: 1;
    letter-spacing: 1px;
  }
  .company-name {
    position: absolute;
    right: 53px;
    top: 108px;
    margin: 0;
    font-size: 31px;
    font-weight: 700;
    color: var(--red);
    line-height: 1;
  }
  .contact {
    position: absolute;
    right: 58px;
    top: 1145px;
    color: var(--white);
    font-size: 13.5px;
    font-weight: 700;
    line-height: 25px;
    text-align: right;
  }
  .contact__row span + span::before {
    content: "|";
    margin: 0 14px 0 12px;
  }
</style>
</head>
<body>
  <div class="letterhead">
    <div class="letterhead__texture" role="img" aria-label="Faint diamond lattice pattern across the page"></div>

    <svg class="letterhead__bands" width="849" height="1200" viewBox="0 0 849 1200" aria-hidden="true">
      <polygon points="0,0 368,0 467,42 0,99" fill="var(--charcoal)"/>
      <polygon points="368,0 849,0 849,68 467,42" fill="var(--red)"/>
      <polygon points="0,1200 0,1157 849,1078 849,1200" fill="var(--charcoal)"/>
      <polygon points="0,1125 325,1149 85,1200 0,1200" fill="var(--red)"/>
    </svg>

    <div class="brand">
      <div class="brand__name">Lumo Fund</div>
      <div class="brand__dot"></div>
    </div>

    <h1 class="company-name">Comapny name's</h1>

    <div class="contact">
      <div class="contact__row"><span>Your Postal Address is here :</span><span>Your contact number :</span></div>
      <div class="contact__row"><span>abced124563@yourwebsite.com :</span><span>www.yourwebsite.com :</span></div>
    </div>
  </div>
</body>
</html>
```